Graphic background for 10 Pull Up Banners

To produce a graphic background for a 100 cm wide by 200 cm high Pull-Up Display banner containing a Buddhist text in three languages: Tibetan, Mandarin and English. Please refer to uploaded file "Elements of Pull Up Banner". The design should be simple (not drawing attention away from the text). This design should then be varied for or extended to the next banner and so on until the 10th banner. When the banners are lined up, they should form a single design that is 1000 cm wide by 200 cm high.
An alternative way to look at the project is to produce a graphic background of 1000 cm width by 200 cm height that is then splitted into ten separate 100 cm wide by 200 cm high graphic to be used as background for 10 Buddhist texts (text 1, 2, 3, 4, 5, 6, 7, 8, 9a, 9b) on 10 Pull-Up Display Banners, the text in each banner being in the three languages mentioned earlier.
In either perspective, the design should be simple and not draw attention away from the texts. See uploaded PDF file "Examples.pdf"
For attendees at a Buddhist Event.

```html
<!DOCTYPE html>
<html lang="en">
<head>
<meta charset="utf-8">
<title>Ten Mistaking – Banner Series</title>
<link href="https://fonts.googleapis.com/css2?family=Questrial&family=Noto+Sans+SC:wght@400&family=Noto+Serif+Tibetan&display=swap" rel="stylesheet">
<style>
  :root{
    --page:#ffffff;
    --banner:#ffffff;
    --ink:#2b2b2b;
    --title:#444444;
    --mark:#c9676b;
    --footer:#2f4a1e;
    --footer-ink:#e8eee0;
    --en-ink:#f1f5ea;
    --panel:rgba(255,255,255,0.2);
    --g-deep:#4f7a2a;
    --g-mid:#74a33a;
    --g-light:#9cc556;
    --g-pale:#c8df8c;
    --g-mist:#a8b89a;
    --water:#bfe3e6;
  }
  *{margin:0;padding:0;box-sizing:border-box}
  html,body{width:1200px;height:287px;overflow:hidden;background:var(--page)}
  .series{display:flex;gap:9.5px;padding:33px 16px 0}
  .banner{position:relative;flex:0 0 108px;height:217px;background:var(--banner);
    box-shadow:0 1px 3px rgba(0,0,0,.35);overflow:hidden;font-family:"Questrial",sans-serif;color:var(--ink)}

  .scene{position:absolute;left:0;right:0;top:0;bottom:23px}
  .banner:nth-child(1) .scene{background:linear-gradient(to bottom,var(--banner) 22%,var(--g-mid) 34%,var(--g-deep) 60%,var(--g-mid) 100%)}
  .banner:nth-child(2) .scene{background:linear-gradient(to bottom,var(--banner) 22%,var(--g-mist) 34%,var(--g-deep) 62%,var(--g-mid) 100%)}
  .banner:nth-child(3) .scene{background:linear-gradient(to bottom,var(--banner) 22%,var(--g-mid) 34%,var(--g-deep) 58%,var(--g-mid) 100%)}
  .banner:nth-child(4) .scene{background:linear-gradient(to bottom,var(--banner) 26%,var(--g-mist) 40%,var(--g-deep) 60%,var(--g-mid) 100%)}
  .banner:nth-child(5) .scene{background:linear-gradient(to bottom,var(--banner) 32%,var(--g-mid) 46%,var(--g-mid) 70%,var(--g-light) 100%)}
  .banner:nth-child(6) .scene{background:linear-gradient(to bottom,var(--banner) 38%,var(--g-light) 50%,var(--g-mid) 75%,var(--g-light) 100%)}
  .banner:nth-child(7) .scene{background:linear-gradient(to bottom,var(--banner) 40%,var(--g-light) 52%,var(--g-mid) 75%,var(--g-light) 100%)}
  .banner:nth-child(8) .scene{background:linear-gradient(to bottom,var(--banner) 40%,var(--g-pale) 50%,var(--g-mid) 74%,var(--g-light) 90%,var(--water) 100%)}
  .banner:nth-child(9) .scene{background:linear-gradient(to bottom,var(--banner) 38%,var(--g-pale) 48%,var(--g-mid) 74%,var(--g-light) 90%,var(--water) 100%)}
  .banner:nth-child(10) .scene{background:linear-gradient(to bottom,var(--banner) 34%,var(--g-pale) 46%,var(--g-mid) 74%,var(--g-light) 90%,var(--water) 100%)}

  .header{position:absolute;top:10px;left:8px;display:flex;align-items:center;gap:4px}
  .brand{display:flex;flex-direction:column;align-items:center;gap:1px;width:22px}
  .brand-dot{width:17px;height:17px;border-radius:50%;background:var(--mark)}
  .brand-name{font-size:2.4px;color:var(--mark);white-space:nowrap}
  .title{line-height:1.1;color:var(--title)}
  .title-zh{font-family:"Noto Sans SC",sans-serif;font-size:9px}
  .title-en{font-size:8px}

  .panel{position:absolute;left:8px;right:8px;top:60px;bottom:26px;background:var(--panel);border-radius:1px}

  .text{position:absolute;white-space:nowrap;overflow:hidden}
  .text-bo{top:49px;left:38px;right:6px;font-family:"Noto Serif Tibetan",serif;font-size:2.4px;line-height:5.3px;color:#222}
  .text-zh{top:99px;left:38px;right:6px;font-family:"Noto Sans SC",sans-serif;font-size:2.5px;line-height:3.4px;color:#1f2a14}
  .text-zh .note{padding-left:2px}
  .text-en{top:145px;left:8px;right:6px;font-size:2.1px;line-height:3.9px;color:var(--en-ink)}

  .footer{position:absolute;left:0;right:0;bottom:0;height:23px;background:var(--footer);color:var(--footer-ink)}
  .footer-url{position:absolute;left:0;right:0;top:4px;text-align:center;font-size:2.8px}
  .footer-zh{position:absolute;left:0;right:0;top:9px;text-align:center;font-family:"Noto Sans SC",sans-serif;font-size:2.3px}
  .footer-wish{position:absolute;left:8px;top:15px;font-size:2.2px}
</style>
</head>
<body>
<main class="series">

<section class="banner">
  <div class="scene" role="img" aria-label="Soft blurred green mountain landscape"></div>
  <header class="header"><div class="brand"><span class="brand-dot"></span><span class="brand-name">Lotus Vale Circle</span></div><div class="title"><div class="title-zh">十个口解</div><div class="title-en">Ten Mistaking</div></div></header>
  <div class="panel"></div>
  <p class="text text-bo" lang="bo">བྱང་ཆུབ་སེམས་ནི་རིན་པོ་ཆེ།<br>མ་སྐྱེས་པ་རྣམས་སྐྱེ་གྱུར་ཅིག།<br>སྐྱེས་པ་ཉམས་པ་མེད་པ་ཡང་།<br>གོང་ནས་གོང་དུ་འཕེལ་བར་ཤོག།<br>སེམས་ཅན་ཐམས་ཅད་བདེ་བ་དང་།<br>བདེ་བའི་རྒྱུ་དང་ལྡན་པར་ཤོག།<br>སྡུག་བསྔལ་དང་ནི་བྲལ་བར་ཤོག།<br>བདེ་བ་དམ་པ་ཐོབ་པར་ཤོག།<br>བཏང་སྙོམས་ཆེན་པོ་ལ་གནས་ཤོག།</p>
  <p class="text text-zh" lang="zh">愿众生远离痛苦，<br>愿众生具足安乐，<br>愿众生心怀慈悲不舍离，<br>愿众生常住平和，<br>愿众生智慧增长，<br>愿众生同得解脱，<br>愿众生远离贪嗔，<br>愿众生安住正念。<br><span class="note">注：愿一切吉祥圆满，</span><br><span class="note">注：愿众生常行善业。</span></p>
  <p class="text text-en">May all beings be free from suffering and its causes.<br>May all beings find lasting peace and quiet joy.<br>May all beings rest in open and steady kindness.<br>May all beings let go of anger and of craving.<br>May all beings meet wisdom on every path.<br>May all beings walk gently with one another.<br>May all beings hold a calm and clear mind.<br>May all beings share in the merit of this day.<br>May all beings find shelter in compassion.<br>May all beings awaken, each and every one.</p>
  <footer class="footer"><span class="footer-url">www.lotusvale.example</span><span class="footer-zh">愿众生同得解脱</span><span class="footer-wish">May all beings be free together</span></footer>
</section>

<section class="banner">
  <div class="scene" role="img" aria-label="Soft blurred green mountain landscape"></div>
  <header class="header"><div class="brand"><span class="brand-dot"></span><span class="brand-name">Lotus Vale Circle</span></div><div class="title"><div class="title-zh">十个口解</div><div class="title-en">Ten Mistaking</div></div></header>
  <div class="panel"></div>
  <p class="text text-bo" lang="bo">བྱང་ཆུབ་སེམས་ནི་རིན་པོ་ཆེ།<br>མ་སྐྱེས་པ་རྣམས་སྐྱེ་གྱུར་ཅིག།<br>སྐྱེས་པ་ཉམས་པ་མེད་པ་ཡང་།<br>གོང་ནས་གོང་དུ་འཕེལ་བར་ཤོག།<br>སེམས་ཅན་ཐམས་ཅད་བདེ་བ་དང་།<br>བདེ་བའི་རྒྱུ་དང་ལྡན་པར་ཤོག།<br>སྡུག་བསྔལ་དང་ནི་བྲལ་བར་ཤོག།<br>བདེ་བ་དམ་པ་ཐོབ་པར་ཤོག།<br>བཏང་སྙོམས་ཆེན་པོ་ལ་གནས་ཤོག།</p>
  <p class="text text-zh" lang="zh">愿众生远离痛苦，<br>愿众生具足安乐，<br>愿众生心怀慈悲不舍离，<br>愿众生常住平和，<br>愿众生智慧增长，<br>愿众生同得解脱，<br>愿众生远离贪嗔，<br>愿众生安住正念。<br><span class="note">注：愿一切吉祥圆满，</span><br><span class="note">注：愿众生常行善业。</span></p>
  <p class="text text-en">May all beings be free from suffering and its causes.<br>May all beings find lasting peace and quiet joy.<br>May all beings rest in open and steady kindness.<br>May all beings let go of anger and of craving.<br>May all beings meet wisdom on every path.<br>May all beings walk gently with one another.<br>May all beings hold a calm and clear mind.<br>May all beings share in the merit of this day.<br>May all beings find shelter in compassion.<br>May all beings awaken, each and every one.</p>
  <footer class="footer"><span class="footer-url">www.lotusvale.example</span><span class="footer-zh">愿众生同得解脱</span><span class="footer-wish">May all beings be free together</span></footer>
</section>

<section class="banner">
  <div class="scene" role="img" aria-label="Soft blurred green mountain landscape"></div>
  <header class="header"><div class="brand"><span class="brand-dot"></span><span class="brand-name">Lotus Vale Circle</span></div><div class="title"><div class="title-zh">十个口解</div><div class="title-en">Ten Mistaking</div></div></header>
  <div class="panel"></div>
  <p class="text text-bo" lang="bo">བྱང་ཆུབ་སེམས་ནི་རིན་པོ་ཆེ།<br>མ་སྐྱེས་པ་རྣམས་སྐྱེ་གྱུར་ཅིག།<br>སྐྱེས་པ་ཉམས་པ་མེད་པ་ཡང་།<br>གོང་ནས་གོང་དུ་འཕེལ་བར་ཤོག།<br>སེམས་ཅན་ཐམས་ཅད་བདེ་བ་དང་།<br>བདེ་བའི་རྒྱུ་དང་ལྡན་པར་ཤོག།<br>སྡུག་བསྔལ་དང་ནི་བྲལ་བར་ཤོག།<br>བདེ་བ་དམ་པ་ཐོབ་པར་ཤོག།<br>བཏང་སྙོམས་ཆེན་པོ་ལ་གནས་ཤོག།</p>
  <p class="text text-zh" lang="zh">愿众生远离痛苦，<br>愿众生具足安乐，<br>愿众生心怀慈悲不舍离，<br>愿众生常住平和，<br>愿众生智慧增长，<br>愿众生同得解脱，<br>愿众生远离贪嗔，<br>愿众生安住正念。<br><span class="note">注：愿一切吉祥圆满，</span><br><span class="note">注：愿众生常行善业。</span></p>
  <p class="text text-en">May all beings be free from suffering and its causes.<br>May all beings find lasting peace and quiet joy.<br>May all beings rest in open and steady kindness.<br>May all beings let go of anger and of craving.<br>May all beings meet wisdom on every path.<br>May all beings walk gently with one another.<br>May all beings hold a calm and clear mind.<br>May all beings share in the merit of this day.<br>May all beings find shelter in compassion.<br>May all beings awaken, each and every one.</p>
  <footer class="footer"><span class="footer-url">www.lotusvale.example</span><span class="footer-zh">愿众生同得解脱</span><span class="footer-wish">May all beings be free together</span></footer>
</section>

<section class="banner">
  <div class="scene" role="img" aria-label="Soft blurred green hillside landscape"></div>
  <header class="header"><div class="brand"><span class="brand-dot"></span><span class="brand-name">Lotus Vale Circle</span></div><div class="title"><div class="title-zh">十个口解</div><div class="title-en">Ten Mistaking</div></div></header>
  <div class="panel"></div>
  <p class="text text-bo" lang="bo">བྱང་ཆུབ་སེམས་ནི་རིན་པོ་ཆེ།<br>མ་སྐྱེས་པ་རྣམས་སྐྱེ་གྱུར་ཅིག།<br>སྐྱེས་པ་ཉམས་པ་མེད་པ་ཡང་།<br>གོང་ནས་གོང་དུ་འཕེལ་བར་ཤོག།<br>སེམས་ཅན་ཐམས་ཅད་བདེ་བ་དང་།<br>བདེ་བའི་རྒྱུ་དང་ལྡན་པར་ཤོག།<br>སྡུག་བསྔལ་དང་ནི་བྲལ་བར་ཤོག།<br>བདེ་བ་དམ་པ་ཐོབ་པར་ཤོག།<br>བཏང་སྙོམས་ཆེན་པོ་ལ་གནས་ཤོག།</p>
  <p class="text text-zh" lang="zh">愿众生远离痛苦，<br>愿众生具足安乐，<br>愿众生心怀慈悲不舍离，<br>愿众生常住平和，<br>愿众生智慧增长，<br>愿众生同得解脱，<br>愿众生远离贪嗔，<br>愿众生安住正念。<br><span class="note">注：愿一切吉祥圆满，</span><br><span class="note">注：愿众生常行善业。</span></p>
  <p class="text text-en">May all beings be free from suffering and its causes.<br>May all beings find lasting peace and quiet joy.<br>May all beings rest in open and steady kindness.<br>May all beings let go of anger and of craving.<br>May all beings meet wisdom on every path.<br>May all beings walk gently with one another.<br>May all beings hold a calm and clear mind.<br>May all beings share in the merit of this day.<br>May all beings find shelter in compassion.<br>May all beings awaken, each and every one.</p>
  <footer class="footer"><span class="footer-url">www.lotusvale.example</span><span class="footer-zh">愿众生同得解脱</span><span class="footer-wish">May all beings be free together</span></footer>
</section>

<section class="banner">
  <div class="scene" role="img" aria-label="Soft blurred green meadow landscape"></div>
  <header class="header"><div class="brand"><span class="brand-dot"></span><span class="brand-name">Lotus Vale Circle</span></div><div class="title"><div class="title-zh">十个口解</div><div class="title-en">Ten Mistaking</div></div></header>
  <div class="panel"></div>
  <p class="text text-bo" lang="bo">བྱང་ཆུབ་སེམས་ནི་རིན་པོ་ཆེ།<br>མ་སྐྱེས་པ་རྣམས་སྐྱེ་གྱུར་ཅིག།<br>སྐྱེས་པ་ཉམས་པ་མེད་པ་ཡང་།<br>གོང་ནས་གོང་དུ་འཕེལ་བར་ཤོག།<br>སེམས་ཅན་ཐམས་ཅད་བདེ་བ་དང་།<br>བདེ་བའི་རྒྱུ་དང་ལྡན་པར་ཤོག།<br>སྡུག་བསྔལ་དང་ནི་བྲལ་བར་ཤོག།<br>བདེ་བ་དམ་པ་ཐོབ་པར་ཤོག།<br>བཏང་སྙོམས་ཆེན་པོ་ལ་གནས་ཤོག།</p>
  <p class="text text-zh" lang="zh">愿众生远离痛苦，<br>愿众生具足安乐，<br>愿众生心怀慈悲不舍离，<br>愿众生常住平和，<br>愿众生智慧增长，<br>愿众生同得解脱，<br>愿众生远离贪嗔，<br>愿众生安住正念。<br><span class="note">注：愿一切吉祥圆满，</span><br><span class="note">注：愿众生常行善业。</span></p>
  <p class="text text-en">May all beings be free from suffering and its causes.<br>May all beings find lasting peace and quiet joy.<br>May all beings rest in open and steady kindness.<br>May all beings let go of anger and of craving.<br>May all beings meet wisdom on every path.<br>May all beings walk gently with one another.<br>May all beings hold a calm and clear mind.<br>May all beings share in the merit of this day.<br>May all beings find shelter in compassion.<br>May all beings awaken, each and every one.</p>
  <footer class="footer"><span class="footer-url">www.lotusvale.example</span><span class="footer-zh">愿众生同得解脱</span><span class="footer-wish">May all beings be free together</span></footer>
</section>

<section class="banner">
  <div class="scene" role="img" aria-label="Soft blurred green meadow landscape"></div>
  <header class="header"><div class="brand"><span class="brand-dot"></span><span class="brand-name">Lotus Vale Circle</span></div><div class="title"><div class="title-zh">十个口解</div><div class="title-en">Ten Mistaking</div></div></header>
  <div class="panel"></div>
  <p class="text text-bo" lang="bo">བྱང་ཆུབ་སེམས་ནི་རིན་པོ་ཆེ།<br>མ་སྐྱེས་པ་རྣམས་སྐྱེ་གྱུར་ཅིག།<br>སྐྱེས་པ་ཉམས་པ་མེད་པ་ཡང་།<br>གོང་ནས་གོང་དུ་འཕེལ་བར་ཤོག།<br>སེམས་ཅན་ཐམས་ཅད་བདེ་བ་དང་།<br>བདེ་བའི་རྒྱུ་དང་ལྡན་པར་ཤོག།<br>སྡུག་བསྔལ་དང་ནི་བྲལ་བར་ཤོག།<br>བདེ་བ་དམ་པ་ཐོབ་པར་ཤོག།<br>བཏང་སྙོམས་ཆེན་པོ་ལ་གནས་ཤོག།</p>
  <p class="text text-zh" lang="zh">愿众生远离痛苦，<br>愿众生具足安乐，<br>愿众生心怀慈悲不舍离，<br>愿众生常住平和，<br>愿众生智慧增长，<br>愿众生同得解脱，<br>愿众生远离贪嗔，<br>愿众生安住正念。<br><span class="note">注：愿一切吉祥圆满，</span><br><span class="note">注：愿众生常行善业。</span></p>
  <p class="text text-en">May all beings be free from suffering and its causes.<br>May all beings find lasting peace and quiet joy.<br>May all beings rest in open and steady kindness.<br>May all beings let go of anger and of craving.<br>May all beings meet wisdom on every path.<br>May all beings walk gently with one another.<br>May all beings hold a calm and clear mind.<br>May all beings share in the merit of this day.<br>May all beings find shelter in compassion.<br>May all beings awaken, each and every one.</p>
  <footer class="footer"><span class="footer-url">www.lotusvale.example</span><span class="footer-zh">愿众生同得解脱</span><span class="footer-wish">May all beings be free together</span></footer>
</section>

<section class="banner">
  <div class="scene" role="img" aria-label="Soft blurred green meadow landscape"></div>
  <header class="header"><div class="brand"><span class="brand-dot"></span><span class="brand-name">Lotus Vale Circle</span></div><div class="title"><div class="title-zh">十个口解</div><div class="title-en">Ten Mistaking</div></div></header>
  <div class="panel"></div>
  <p class="text text-bo" lang="bo">བྱང་ཆུབ་སེམས་ནི་རིན་པོ་ཆེ།<br>མ་སྐྱེས་པ་རྣམས་སྐྱེ་གྱུར་ཅིག།<br>སྐྱེས་པ་ཉམས་པ་མེད་པ་ཡང་།<br>གོང་ནས་གོང་དུ་འཕེལ་བར་ཤོག།<br>སེམས་ཅན་ཐམས་ཅད་བདེ་བ་དང་།<br>བདེ་བའི་རྒྱུ་དང་ལྡན་པར་ཤོག།<br>སྡུག་བསྔལ་དང་ནི་བྲལ་བར་ཤོག།<br>བདེ་བ་དམ་པ་ཐོབ་པར་ཤོག།<br>བཏང་སྙོམས་ཆེན་པོ་ལ་གནས་ཤོག།</p>
  <p class="text text-zh" lang="zh">愿众生远离痛苦，<br>愿众生具足安乐，<br>愿众生心怀慈悲不舍离，<br>愿众生常住平和，<br>愿众生智慧增长，<br>愿众生同得解脱，<br>愿众生远离贪嗔，<br>愿众生安住正念。<br><span class="note">注：愿一切吉祥圆满，</span><br><span class="note">注：愿众生常行善业。</span></p>
  <p class="text text-en">May all beings be free from suffering and its causes.<br>May all beings find lasting peace and quiet joy.<br>May all beings rest in open and steady kindness.<br>May all beings let go of anger and of craving.<br>May all beings meet wisdom on every path.<br>May all beings walk gently with one another.<br>May all beings hold a calm and clear mind.<br>May all beings share in the merit of this day.<br>May all beings find shelter in compassion.<br>May all beings awaken, each and every one.</p>
  <footer class="footer"><span class="footer-url">www.lotusvale.example</span><span class="footer-zh">愿众生同得解脱</span><span class="footer-wish">May all beings be free together</span></footer>
</section>

<section class="banner">
  <div class="scene" role="img" aria-label="Soft blurred green meadow by water"></div>
  <header class="header"><div class="brand"><span class="brand-dot"></span><span class="brand-name">Lotus Vale Circle</span></div><div class="title"><div class="title-zh">十个口解</div><div class="title-en">Ten Mistaking</div></div></header>
  <div class="panel"></div>
  <p class="text text-bo" lang="bo">བྱང་ཆུབ་སེམས་ནི་རིན་པོ་ཆེ།<br>མ་སྐྱེས་པ་རྣམས་སྐྱེ་གྱུར་ཅིག།<br>སྐྱེས་པ་ཉམས་པ་མེད་པ་ཡང་།<br>གོང་ནས་གོང་དུ་འཕེལ་བར་ཤོག།<br>སེམས་ཅན་ཐམས་ཅད་བདེ་བ་དང་།<br>བདེ་བའི་རྒྱུ་དང་ལྡན་པར་ཤོག།<br>སྡུག་བསྔལ་དང་ནི་བྲལ་བར་ཤོག།<br>བདེ་བ་དམ་པ་ཐོབ་པར་ཤོག།<br>བཏང་སྙོམས་ཆེན་པོ་ལ་གནས་ཤོག།</p>
  <p class="text text-zh" lang="zh">愿众生远离痛苦，<br>愿众生具足安乐，<br>愿众生心怀慈悲不舍离，<br>愿众生常住平和，<br>愿众生智慧增长，<br>愿众生同得解脱，<br>愿众生远离贪嗔，<br>愿众生安住正念。<br><span class="note">注：愿一切吉祥圆满，</span><br><span class="note">注：愿众生常行善业。</span></p>
  <p class="text text-en">May all beings be free from suffering and its causes.<br>May all beings find lasting peace and quiet joy.<br>May all beings rest in open and steady kindness.<br>May all beings let go of anger and of craving.<br>May all beings meet wisdom on every path.<br>May all beings walk gently with one another.<br>May all beings hold a calm and clear mind.<br>May all beings share in the merit of this day.<br>May all beings find shelter in compassion.<br>May all beings awaken, each and every one.</p>
  <footer class="footer"><span class="footer-url">www.lotusvale.example</span><span class="footer-zh">愿众生同得解脱</span><span class="footer-wish">May all beings be free together</span></footer>
</section>

<section class="banner">
  <div class="scene" role="img" aria-label="Soft blurred green meadow by water"></div>
  <header class="header"><div class="brand"><span class="brand-dot"></span><span class="brand-name">Lotus Vale Circle</span></div><div class="title"><div class="title-zh">十个口解</div><div class="title-en">Ten Mistaking</div></div></header>
  <div class="panel"></div>
  <p class="text text-bo" lang="bo">བྱང་ཆུབ་སེམས་ནི་རིན་པོ་ཆེ།<br>མ་སྐྱེས་པ་རྣམས་སྐྱེ་གྱུར་ཅིག།<br>སྐྱེས་པ་ཉམས་པ་མེད་པ་ཡང་།<br>གོང་ནས་གོང་དུ་འཕེལ་བར་ཤོག།<br>སེམས་ཅན་ཐམས་ཅད་བདེ་བ་དང་།<br>བདེ་བའི་རྒྱུ་དང་ལྡན་པར་ཤོག།<br>སྡུག་བསྔལ་དང་ནི་བྲལ་བར་ཤོག།<br>བདེ་བ་དམ་པ་ཐོབ་པར་ཤོག།<br>བཏང་སྙོམས་ཆེན་པོ་ལ་གནས་ཤོག།</p>
  <p class="text text-zh" lang="zh">愿众生远离痛苦，<br>愿众生具足安乐，<br>愿众生心怀慈悲不舍离，<br>愿众生常住平和，<br>愿众生智慧增长，<br>愿众生同得解脱，<br>愿众生远离贪嗔，<br>愿众生安住正念。<br><span class="note">注：愿一切吉祥圆满，</span><br><span class="note">注：愿众生常行善业。</span></p>
  <p class="text text-en">May all beings be free from suffering and its causes.<br>May all beings find lasting peace and quiet joy.<br>May all beings rest in open and steady kindness.<br>May all beings let go of anger and of craving.<br>May all beings meet wisdom on every path.<br>May all beings walk gently with one another.<br>May all beings hold a calm and clear mind.<br>May all beings share in the merit of this day.<br>May all beings find shelter in compassion.<br>May all beings awaken, each and every one.</p>
  <footer class="footer"><span class="footer-url">www.lotusvale.example</span><span class="footer-zh">愿众生同得解脱</span><span class="footer-wish">May all beings be free together</span></footer>
</section>

<section class="banner">
  <div class="scene" role="img" aria-label="Soft blurred green meadow by water"></div>
  <header class="header"><div class="brand"><span class="brand-dot"></span><span class="brand-name">Lotus Vale Circle</span></div><div class="title"><div class="title-zh">十个口解</div><div class="title-en">Ten Mistaking</div></div></header>
  <div class="panel"></div>
  <p class="text text-bo" lang="bo">བྱང་ཆུབ་སེམས་ནི་རིན་པོ་ཆེ།<br>མ་སྐྱེས་པ་རྣམས་སྐྱེ་གྱུར་ཅིག།<br>སྐྱེས་པ་ཉམས་པ་མེད་པ་ཡང་།<br>གོང་ནས་གོང་དུ་འཕེལ་བར་ཤོག།<br>སེམས་ཅན་ཐམས་ཅད་བདེ་བ་དང་།<br>བདེ་བའི་རྒྱུ་དང་ལྡན་པར་ཤོག།<br>སྡུག་བསྔལ་དང་ནི་བྲལ་བར་ཤོག།<br>བདེ་བ་དམ་པ་ཐོབ་པར་ཤོག།<br>བཏང་སྙོམས་ཆེན་པོ་ལ་གནས་ཤོག།</p>
  <p class="text text-zh" lang="zh">愿众生远离痛苦，<br>愿众生具足安乐，<br>愿众生心怀慈悲不舍离，<br>愿众生常住平和，<br>愿众生智慧增长，<br>愿众生同得解脱，<br>愿众生远离贪嗔，<br>愿众生安住正念。<br><span class="note">注：愿一切吉祥圆满，</span><br><span class="note">注：愿众生常行善业。</span></p>
  <p class="text text-en">May all beings be free from suffering and its causes.<br>May all beings find lasting peace and quiet joy.<br>May all beings rest in open and steady kindness.<br>May all beings let go of anger and of craving.<br>May all beings meet wisdom on every path.<br>May all beings walk gently with one another.<br>May all beings hold a calm and clear mind.<br>May all beings share in the merit of this day.<br>May all beings find shelter in compassion.<br>May all beings awaken, each and every one.</p>
  <footer class="footer"><span class="footer-url">www.lotusvale.example</span><span class="footer-zh">愿众生同得解脱</span><span class="footer-wish">May all beings be free together</span></footer>
</section>

</main>
</body>
</html>
```